Boracay Wedding Invitation Design

Hello, We would like a wedding invitation design for our wedding in Boracay. We would like it somewhat in the form of a boarding pass with beachy fresh colours, possibly a nice Boracay beach in the background Double sided with an envelope design to match. Maybe something simple on the envelope like a nice picture in the bottom left corner of a shell on a beach or something similar.

I would also like on the opposite side of the invite to be an "information sheet" with a matching beach design

The text files for both sides are included and i have also included 2 designs that i thought looked nice and are similar to what we are after.
Updates

Hello, I have updated the brief to be more specific with text files and images to make it easier for you. Thank you :)

Industry/Entity Type

Wedding

Font styles to use
Decorative
Script

Colors
fbee3d
33a6d7
33b8a4
fbf289
85cae6
ffffff

Requirements
Must have
• I would like to have this quote somewhere on the invitation
• This day I will marry my best friend,
• the one I laugh with,
• live for,
• dream with,
• love
• Owen & Marisa
• Request the pleasure of your company to celebrate their wedding
• On Friday the 17th March 2017
• at
• Velora Grand Suites
• Boracay, Philippines
• Ceremony begins at 3.00pm
• RSVP
• Owen 0437291856
• Marisa 0418273940
• by
• 17th Jan 2016
• Dress: Beach Formal
• For the "information sheet"
• There will be a 5% discount on rooms booked at the Velora under the event Owen & Marisa Wedding. The resort has a total of 24 rooms it would be nice if the majority of guests could stay at the resort from the night before until the night after the wedding but if you choose to stay elsewhere on the island there are plenty of other places to stay for cheaper and everything is fairly close as its a small island.
• We have currently blocked room stay for a short period of time so our guests can book rooms. If you choose to do so please email reservations@veloraresorts-example.com. Once rooms become available to the public again, towards the end of Jan, it will be first come first served basis. The resort is very popular so im assuming once this happens the rooms will be booked out.
• If you would like to check out the resort itself the website is www.veloragrand-example.com
• We know its a fair distance to travel but we would really love to see you all there to celebrate and maybe even enjoy a small holiday while your here its a beautiful part of the world.
• If anyone has any questions please feel free to contact Owen on 0437291856
Nice to have
• A nice picture of a Boracay beach in the background would be nice

```html
<!DOCTYPE html>
<html lang="en">
<head>
<meta charset="utf-8">
<title>Owen &amp; Marisa – Boarding Pass Wedding Invitation</title>
<link rel="stylesheet" href="https://fonts.googleapis.com/css2?family=Alegreya:wght@400&family=Great+Vibes&display=swap">
<style>
  :root {
    --sky: #33a6d7;
    --lagoon: #85cae6;
    --sand: #fbf289;
    --sun: #fbee3d;
    --white: #ffffff;
    --paper: #ffffff;
    --shell: #6fc1d9;
    --body-font: "Alegreya", serif;
    --script-font: "Great Vibes", cursive;
  }
  * { box-sizing: border-box; margin: 0; padding: 0; }
  html, body {
    width: 1200px; height: 705px; overflow: hidden;
    background: var(--paper);
  }
  .canvas { position: relative; width: 1200px; height: 705px; }

  .pass {
    position: absolute;
    border: 1.5px solid var(--sky);
    border-radius: 20px;
    overflow: hidden;
    color: var(--white);
    font-family: var(--body-font);
  }
  .pass__scene { position: absolute; inset: 0; width: 100%; height: 100%; }

  /* front */
  .pass--front { left: 554px; top: 0; width: 625px; height: 295px; }
  .perforation {
    position: absolute; top: 0; bottom: 0; width: 0;
    border-left: 1.5px dashed var(--white);
  }
  .perforation--left { left: 37px; }
  .perforation--right { left: 467px; }

  .side-label {
    position: absolute;
    writing-mode: vertical-rl;
    transform: rotate(180deg);
    font-size: 9px;
    letter-spacing: 4.5px;
    color: var(--white);
    white-space: nowrap;
  }
  .pass--front .side-label { left: 18px; top: 30px; height: 235px; text-align: center; }

  .sun { position: absolute; border-radius: 50%; background: var(--sun); }
  .pass--front .sun { left: 69px; top: 41px; width: 60px; height: 60px; }

  .invite {
    position: absolute; left: 38px; width: 429px; top: 0; height: 295px;
    text-align: center; font-size: 11.5px;
  }
  .invite__line { position: absolute; left: 0; right: 0; line-height: 12px; white-space: nowrap; }
  .invite__names {
    font-family: var(--script-font);
    font-size: 26px; line-height: 28px;
  }

  .stub {
    position: absolute; left: 468px; width: 157px; top: 0; height: 295px;
    text-align: center; font-size: 11.5px;
  }
  .stub__line { position: absolute; left: 0; right: 0; line-height: 12px; white-space: nowrap; }
  .stub__heart { position: absolute; left: 38px; top: 30px; width: 82px; height: 84px; }
  .stub__seat-number {
    position: absolute; left: 0; right: 0; top: 48px;
    font-family: var(--script-font); font-size: 34px; line-height: 1;
  }

  .shell-art {
    position: absolute;
    background: var(--shell);
    opacity: 0.55;
    border-radius: 50% 50% 12px 12px;
  }

  /* back */
  .pass--back { left: 546px; top: 397px; width: 622px; height: 295px; }
  .pass--back .sun { left: 22px; top: 10px; width: 58px; height: 58px; }
  .pass--back .side-label { left: 20px; top: 8px; height: 278px; text-align: center; letter-spacing: 4px; }
  .pass--back .info-heart { position: absolute; left: 522px; top: 6px; width: 94px; height: 110px; }

  .info {
    position: absolute; left: 92px; top: 0; width: 420px; height: 295px;
    font-size: 10.5px;
  }
  .info__line {
    position: absolute; left: 0; width: 420px;
    line-height: 12px; white-space: nowrap;
  }
  .info__line--full { text-align: justify; text-align-last: justify; }
</style>
</head>
<body>
<main class="canvas">

  <!-- Front: invitation boarding pass -->
  <section class="pass pass--front" aria-label="Wedding invitation boarding pass">
    <svg class="pass__scene" viewBox="0 0 625 295" preserveAspectRatio="none" aria-hidden="true">
      <rect width="625" height="295" fill="var(--sky)"/>
      <path d="M0 148 C120 136 220 158 330 148 S520 138 625 150 L625 295 L0 295 Z" fill="var(--lagoon)"/>
      <path d="M0 228 C110 220 230 236 340 228 S520 222 625 230 L625 295 L0 295 Z" fill="var(--sand)"/>
    </svg>

    <span class="perforation perforation--left"></span>
    <span class="perforation perforation--right"></span>
    <span class="side-label">WEDDING INVITATION</span>
    <span class="sun"></span>

    <div class="invite">
      <p class="invite__line" style="top:17px">This day I will marry my best friend,</p>
      <p class="invite__line" style="top:35px">the one I laugh with,</p>
      <p class="invite__line" style="top:53px">live for,</p>
      <p class="invite__line" style="top:70px">dream with,</p>
      <p class="invite__line" style="top:88px">love</p>
      <p class="invite__line invite__names" style="top:112px">Owen &amp; Marisa</p>
      <p class="invite__line" style="top:158px">Request the pleasure of your company to celebrate their wedding</p>
      <p class="invite__line" style="top:176px">On Friday the 17th March 2017</p>
      <p class="invite__line" style="top:193px">at</p>
      <p class="invite__line" style="top:210px">Velora Grand Suites</p>
      <p class="invite__line" style="top:228px">Boracay, Philippines</p>
      <p class="invite__line" style="top:264px">Ceremony begins at 3.00pm</p>
    </div>

    <div class="stub">
      <p class="stub__line" style="top:15px">CONFIRMED</p>
      <svg class="stub__heart" viewBox="0 0 82 84" aria-hidden="true">
        <path d="M41 80 C30 64 4 50 4 27 C4 11 16 4 27 4 C35 4 40 10 41 16 C42 10 47 4 55 4 C66 4 78 11 78 27 C78 50 52 64 41 80 Z"
              fill="none" stroke="var(--white)" stroke-width="1.6"/>
      </svg>
      <p class="stub__seat-number">63</p>
      <p class="stub__line" style="top:116px">SEAT</p>
      <p class="stub__line" style="top:154px">Dress: Beach Formal</p>
      <p class="stub__line" style="top:193px">RSVP</p>
      <p class="stub__line" style="top:210px">Owen 0437291856</p>
      <p class="stub__line" style="top:229px">Marisa 0418273940</p>
      <p class="stub__line" style="top:246px">by</p>
      <p class="stub__line" style="top:264px">17th Jan 2016</p>
    </div>

    <div class="shell-art" role="img" aria-label="Seashell illustration" style="left:10px; top:254px; width:70px; height:32px;"></div>
    <div class="shell-art" role="img" aria-label="Seashell illustration" style="left:408px; top:248px; width:50px; height:40px;"></div>
  </section>

  <!-- Back: guest information sheet -->
  <section class="pass pass--back" aria-label="Guest information sheet">
    <svg class="pass__scene" viewBox="0 0 622 295" preserveAspectRatio="none" aria-hidden="true">
      <rect width="622" height="295" fill="var(--sky)"/>
      <path d="M0 146 C120 134 220 156 330 148 S520 138 622 150 L622 295 L0 295 Z" fill="var(--lagoon)"/>
      <path d="M0 220 C110 212 230 228 340 220 S520 214 622 222 L622 295 L0 295 Z" fill="var(--sand)"/>
    </svg>

    <span class="sun"></span>
    <span class="side-label">LAUGH. LIVE. DREAM. LOVE</span>

    <svg class="info-heart" viewBox="0 0 94 110" aria-hidden="true">
      <path d="M47 104 C34 84 6 66 6 36 C6 16 20 6 33 6 C42 6 46 14 47 22 C48 14 54 6 63 6 C76 6 88 16 88 36 C88 66 60 84 47 104 Z"
            fill="none" stroke="var(--white)" stroke-width="1.8"/>
    </svg>

    <div class="info">
      <p class="info__line info__line--full" style="top:5px">There will be a 5% discount on rooms booked at the Velora under the event Owen &amp; Marisa Wedding.</p>
      <p class="info__line info__line--full" style="top:22px">The resort has a total of 24 rooms it would be nice if the majority of guests could stay at the resort</p>
      <p class="info__line info__line--full" style="top:39px">from the night before until the night after the wedding but if you choose to stay elsewhere on the</p>
      <p class="info__line info__line--full" style="top:56px">island there are plenty of other places to stay for cheaper and everything is fairly close as its a small</p>
      <p class="info__line" style="top:72px">island.</p>

      <p class="info__line info__line--full" style="top:108px">We have currently blocked room stay for a short period of time so our guests can book rooms. If you</p>
      <p class="info__line info__line--full" style="top:125px">choose to do so please email reservations@veloraresorts-example.com. Once rooms become available to the</p>
      <p class="info__line info__line--full" style="top:141px">public again, towards the end of Jan, it will be first come first served basis. The resort is very popular</p>
      <p class="info__line" style="top:158px">so im assuming once this happens the rooms will be booked out.</p>

      <p class="info__line" style="top:191px">If you would like to check out the resort itself the website is www.veloragrand-example.com</p>

      <p class="info__line info__line--full" style="top:226px">We know its a fair distance to travel but we would really love to see you all there to celebrate and</p>
      <p class="info__line" style="top:243px">maybe even enjoy a small holiday while your here its a beautiful part of the world.</p>

      <p class="info__line" style="top:274px">If anyone has any questions please feel free to contact Owen on 0437291856</p>
    </div>

    <div class="shell-art" role="img" aria-label="Seashell illustration" style="left:450px; top:246px; width:58px; height:28px;"></div>
    <div class="shell-art" role="img" aria-label="Seashell illustration" style="left:542px; top:262px; width:26px; height:22px;"></div>
    <div class="shell-art" role="img" aria-label="Seashell illustration" style="left:570px; top:250px; width:38px; height:32px;"></div>
  </section>

</main>
</body>
</html>
```